Ravelor Global Kft. is an online recruitment marketplace connecting the employers and recruiters together. We provide an e-bussiness solution for companies and give busines opportunity for recruiters.
We have a logo design already, which should be used on the business card.
Our colours are grey and magenta, which can be seen in the logo. Black is also welcome.
The style should be dynamic, young but professional. It should be clear, visible, elegant, not too crowded, simple but exciting.
We need the following data on the BC: name, title, address, phone,fax and mobile number, email address, website.
Target Market(s)
Our target market are companies, as this is a B2B business. We also target recruiters, recruitment professionals, headhunters.We would like to be impressive and different.
Industry/Entity Type
Business
Requirements
Must have
- We would like to promote our website, www.ravelorglb.hu.
- Please, put this on the back with a quite visible letter size.The style should be dynamic, young but professional. It should be clear, visible, elegant, not too crowded, simple but exciting.
Should not have
- We do not want to see people figures.

```html
<!DOCTYPE html>
<html lang="en">
<head>
<meta charset="utf-8">
<title>Ravelor Global Kft. – Business Card</title>
<link rel="stylesheet" href="https://fonts.googleapis.com/css2?family=Arimo:wght@400;700&family=Roboto+Condensed:wght@700&family=Tinos:wght@700&display=swap">
<style>
  :root {
    --page: #ffffff;
    --card: #ffffff;
    --card-edge: #d6d6d6;
    --magenta: #d21fd0;
    --violet: #a10fb5;
    --grey: #6d6790;
    --ink: #4a4a4a;
  }
  * { margin: 0; padding: 0; box-sizing: border-box; }
  html, body {
    width: 1200px; height: 899px; overflow: hidden;
    background: var(--page);
  }
  .sheet { position: relative; width: 1200px; height: 899px; }

  .card {
    position: absolute;
    width: 487px; height: 318px;
    background: var(--card);
    border: 1px solid var(--card-edge);
  }
  .card--front { left: 117px; top: 133px; }
  .card--back  { left: 578px; top: 427px; }

  .brand { position: absolute; display: flex; align-items: flex-end; }
  .brand__square { background: var(--violet); flex: none; }
  .brand__name {
    font-family: "Roboto Condensed", "Arial Narrow", sans-serif;
    font-weight: 700;
    color: var(--violet);
    white-space: nowrap;
    line-height: 1;
  }
  .card--front .brand { left: 60px; top: 64px; gap: 12px; }
  .card--front .brand__square { width: 135px; height: 137px; }
  .card--front .brand__name { font-size: 40px; margin-bottom: 2px; }

  .card--back .brand { left: 38px; top: 190px; gap: 8px; }
  .card--back .brand__square { width: 70px; height: 70px; }
  .card--back .brand__name { font-size: 21px; margin-bottom: 1px; }

  .details {
    position: absolute; right: 44px; top: 72px;
    text-align: right;
    font-family: "Arimo", Arial, sans-serif;
    font-size: 10px; line-height: 1.75;
    color: var(--ink);
  }
  .details__name {
    font-family: "Tinos", "Times New Roman", serif;
    font-weight: 700; font-size: 17px; line-height: 1.2;
    color: var(--magenta);
  }
  .details__title { font-size: 11px; line-height: 1.4; margin-bottom: 42px; color: var(--grey); }
  .details__address { line-height: 1.6; margin-bottom: 12px; }
  .details__label { color: var(--magenta); margin-right: 3px; }
  .details__web {
    font-family: "Tinos", "Times New Roman", serif;
    font-weight: 700; font-size: 12px;
    color: var(--magenta);
  }
</style>
</head>
<body>
<main class="sheet">
  <section class="card card--front" aria-label="Card front">
    <div class="brand">
      <span class="brand__square"></span>
      <span class="brand__name">Ravelor Global</span>
    </div>
  </section>

  <section class="card card--back" aria-label="Card back">
    <div class="details">
      <p class="details__name">Mr Daniel Hart</p>
      <p class="details__title">Recruitment Consultant</p>
      <p class="details__address">1 Any Street, Any Town,<br>Any Country, Zip Code</p>
      <p><span class="details__label">m</span>09871 204 318</p>
      <p><span class="details__label">t</span>01234 765 4102 &nbsp;<span class="details__label">f</span>01234 765 4103</p>
      <p><span class="details__label">e</span>anyone@ravelorglb.hu</p>
      <p class="details__web">www.ravelorglb.hu</p>
    </div>
    <div class="brand">
      <span class="brand__square"></span>
      <span class="brand__name">Ravelor Global</span>
    </div>
  </section>
</main>
</body>
</html>
```